Rack card for a integrative medical practice

Need an eye-catching rack card with our logo with content as provided. We have a membership based holistic medical practice which incorporates western and holistic medicine. We would like to focus on wellness and healthy lifestyle. See uploaded files for what is included in the membership. Would like 2 page rack card color on both sides. Logo must be on the front.

Target Market(s)

People looking for alternative medicine, healthy lifestyle.

Industry/Entity Type

Health and Wellness

Colors
00AB8E
00BBA5
67D7C9
C6EFE9
E9F9F6

Requirements
Must have
• Must spark interest at first sight. Clear message.
Nice to have
• Warm, bright and positive vibe. Organic, neutral and earthy colors.
Should not have
• Traditional medical practice vibe (cold, formal, industrial). No PINK except the logo.

```html
<!DOCTYPE html>
<html lang="en">
<head>
<meta charset="utf-8">
<title>Willow Health &amp; Wellness — Rack Card</title>
<link href="https://fonts.googleapis.com/css2?family=Marcellus&family=Lato:wght@300;400;700&display=swap" rel="stylesheet">
<style>
  :root {
    --backdrop: #ececec;
    --teal-deep: #12ada0;
    --teal: #1fbcae;
    --teal-light: #67d7c9;
    --mint: #c6efe9;
    --mist: #e9f9f6;
    --plum: #6b2466;
    --plum-dark: #4e2152;
    --white: #ffffff;
    --address: #139d94;
  }
  * { box-sizing: border-box; margin: 0; padding: 0; }
  html, body { width: 1200px; height: 800px; overflow: hidden; }
  body {
    background: var(--backdrop);
    position: relative;
    font-family: "Lato", sans-serif;
  }
  .rack-card {
    position: absolute;
    top: 173px;
    width: 215px;
    height: 455px;
    overflow: hidden;
  }
  .rack-card--front { left: 365px; background: var(--white); }
  .rack-card--back {
    left: 621px;
    background: linear-gradient(160deg, var(--teal-light) 0%, var(--teal) 55%, var(--teal-deep) 100%);
    color: var(--white);
    text-align: center;
  }

  /* Front */
  .brand {
    height: 107px;
    display: flex;
    flex-direction: column;
    align-items: center;
    justify-content: center;
    gap: 10px;
    background: radial-gradient(ellipse at 50% 0%, var(--white) 40%, #f1f3f3 100%);
  }
  .brand__mark {
    width: 20px; height: 20px;
    border-radius: 50%;
    background: var(--plum);
  }
  .brand__name {
    font-family: "Lato", sans-serif;
    font-weight: 700;
    color: var(--plum);
    font-size: 15px;
    letter-spacing: 0;
    line-height: 1.2;
  }
  .hero-photo {
    display: block;
    height: 140px;
    background: linear-gradient(120deg, #f3e6e6 0%, #fbf6f4 45%, #e8dbe0 75%, #d9b9c4 100%);
  }
  .mission {
    height: 148px;
    background: linear-gradient(170deg, var(--teal-light) 0%, var(--teal) 60%, var(--teal-deep) 100%);
    display: flex;
    align-items: center;
    justify-content: center;
    padding: 0 10px;
  }
  .mission__text {
    font-family: "Marcellus", serif;
    color: var(--plum);
    font-size: 14px;
    line-height: 17.6px;
    text-align: center;
    text-transform: uppercase;
    -webkit-text-stroke: 0.4px var(--plum);
  }
  .location {
    height: 60px;
    position: relative;
    background: linear-gradient(180deg, var(--white), #f1f3f3);
    text-align: center;
    padding-top: 12px;
  }
  .location__address {
    color: var(--address);
    font-weight: 700;
    font-size: 12px;
    line-height: 14.5px;
    font-style: normal;
  }
  .location__bar {
    position: absolute;
    bottom: 0;
    left: 52px;
    width: 112px;
    height: 10px;
    background: var(--plum-dark);
  }

  /* Back */
  .benefits__title {
    font-family: "Marcellus", serif;
    color: var(--plum);
    font-size: 17.5px;
    line-height: 23px;
    margin-top: 12px;
    font-weight: 400;
    -webkit-text-stroke: 0.4px var(--plum);
  }
  .benefits__list {
    list-style: none;
    margin-top: 19px;
    font-weight: 300;
    font-size: 12.2px;
    line-height: 15.5px;
  }
  .benefits__item { margin-bottom: 10.2px; }
  .benefits__item::before {
    content: "";
    display: inline-block;
    width: 5px; height: 6px;
    margin-right: 3px;
    background: var(--plum);
    border-radius: 50% 50% 50% 50% / 60% 60% 40% 40%;
    clip-path: polygon(50% 0, 100% 60%, 100% 100%, 0 100%, 0 60%);
    vertical-align: 0;
  }
</style>
</head>
<body>
  <section class="rack-card rack-card--front">
    <header class="brand">
      <span class="brand__mark"></span>
      <span class="brand__name">Willow Health &amp; Wellness</span>
    </header>
    <div class="hero-photo" role="img" aria-label="Photo of a person in white clothing sitting cross-legged in meditation, hand on heart, in a bright cushioned room"></div>
    <div class="mission">
      <p class="mission__text">A direct primary<br>care practice<br>focused on a more<br>holistic and personal<br>approach to medicine</p>
    </div>
    <footer class="location">
      <address class="location__address">1420 Ridge Ave., STE 2B<br>Fairview</address>
      <span class="location__bar"></span>
    </footer>
  </section>

  <section class="rack-card rack-card--back">
    <h2 class="benefits__title">WHAT’S INCLUDED IN<br>YOUR MEMBERSHIP:</h2>
    <ul class="benefits__list">
      <li class="benefits__item">Unlimited office visits<br>with no copay</li>
      <li class="benefits__item">Direct communication<br>with your doctor</li>
      <li class="benefits__item">Discounted labs, imaging<br>and medications</li>
      <li class="benefits__item">Free initial acupuncture session<br>($250 value)</li>
      <li class="benefits__item">2 Body composition tests per year<br>($100 value)</li>
      <li class="benefits__item">Discounts for supplements<br>and health products in the clinic</li>
      <li class="benefits__item">Discounts for iv<br>vitamin infusion therapy</li>
      <li class="benefits__item">Personalized nutrition<br>plan after advanced testing<br>such as gut microbiome,<br>hormonal, metabolism test, etc.</li>
    </ul>
  </section>
</body>
</html>
```